Building Maintenance Flyer specialising in hot and silent pressure cleaning

Hi. I love this flyer. I would like something similar but with hot water pressure washing and building maintenance

Ferro Lane & Services provides high pressure steam cleaning and water blasting services throughout Brisbane and surrounding areas, covering the Industrial, Commercial, Strata and Residential property owners sectors.

FLS combining the cleaning power of heat with state-of-the-art silent equipment, accredited technicians and a steadfast commitment to the environment. We offer the best Prompt, Professional Service.

Fully Accredited & Certified Technicians
100% Satisfaction Guaranteed
We are a family owned and operated business and love what we do. No job is too big or too small and we take pride in our work.
All of our services are undertaken using industry leading equipment and, providing safe and superior results.

Our business is covered by 20 million full public liability insurance and we operate within strict health & safety guidelines, providing all our clients with complete peace of mind. Project plans and risk assessments can also be provided upon request.

BODY CORPORATES

BUILDING FAÇADE CLEANING

CAR PARKS – underground, single and multi level

DRIVE THRU

FOOD PRODUCTION FACILITIES CLEANING SANITISING

SHOPPING CENTRES

BIRD MANAGEMENT AND DECONTAMINATION

GENERAL MAINTENANCE

CONSTRUCTION CLEAN UPS

SPILL MANAGEMENT

CONCRETE CLEANING AND DEGRASING

CONCRETE SEALING

FACTORY CLEANING & CLEAN UP

ENVIRONMENTAL DECONTAMINATION OF HEAVY VEHICLES AND EQUIPMENT

SITE CLEANS AND RUBBISH REMOVAL

MANUFACTURING PLANTS

Target Market(s)

Facility Managers, Commercial and Industrial Property Owners, Property Managers, Schools, Restaurants,

Industry/Entity Type

Pressure Cleaning

Font styles to use
Sans Serif

Colors
0293ce
00a990
33a6d7
33b8a4

Requirements
Must have
• SILENT HOT WATER PRESSURE CLEANING
Runs up to 120 Degrees Celsius
SANITISING - Bin areas, outdoor areas, cafe's, restaurants, schools, drive thru's
Blue's and Greens to link in with our logo

```html
<!DOCTYPE html>
<html lang="en">
<head>
<meta charset="utf-8">
<title>Ferro Lane &amp; Services – Commercial &amp; Industrial Property Maintenance</title>
<link rel="stylesheet" href="https://fonts.googleapis.com/css2?family=Open+Sans:ital,wght@0,400;0,600;0,700;0,800;1,700;1,800&family=Roboto:wght@400;500&display=swap">
<style>
  :root {
    --brand-blue: #0293ce;
    --brand-green: #00a990;
    --sky-blue: #33a6d7;
    --sea-green: #33b8a4;
    --deep-blue: #1d4fa0;
    --navy: #163d80;
    --ink: #2a2f3a;
    --white: #ffffff;
    --paper: #eef1f4;
  }
  * { box-sizing: border-box; margin: 0; padding: 0; }
  html, body { width: 877px; height: 1200px; overflow: hidden; background: var(--paper); }
  .flyer {
    position: relative; width: 877px; height: 1200px; overflow: hidden;
    font-family: "Open Sans", Arial, sans-serif; color: var(--ink);
  }
  .flyer-backdrop { position: absolute; inset: 0; width: 877px; height: 1200px; }

  .headline {
    position: absolute; left: 40px; top: 60px; width: 560px;
    color: var(--white); font-style: italic; font-weight: 800;
    font-size: 37px; line-height: 1.12; text-transform: uppercase; letter-spacing: 0.5px;
  }
  .service-area {
    position: absolute; left: 40px; top: 240px; width: 300px;
    color: var(--sea-green); font-weight: 700; font-size: 21px; line-height: 1.18;
  }

  .brand-name {
    position: absolute; left: 40px; top: 540px; width: 380px; text-align: center;
    color: var(--deep-blue); font-weight: 800;
  }
  .brand-name .initials { display: block; font-size: 72px; line-height: 1; letter-spacing: 4px; }
  .brand-name .full { display: block; font-size: 15px; letter-spacing: 2px; margin-top: 4px; }

  .feature {
    position: absolute; left: 40px; top: 660px; width: 400px;
    font-style: italic; font-weight: 800; color: var(--deep-blue); font-size: 18px; line-height: 1.3;
  }
  .feature .temp { display: block; color: var(--brand-green); font-size: 17px; }

  .assurances { position: absolute; left: 40px; top: 730px; list-style: none; width: 400px; }
  .assurances li {
    display: flex; align-items: center; gap: 10px;
    font-weight: 700; color: var(--deep-blue); font-size: 15.5px; line-height: 1; margin-bottom: 13px;
  }
  .assurances svg { flex: none; }

  .equipment-note {
    position: absolute; left: 40px; top: 862px; width: 390px;
    color: var(--deep-blue); font-size: 15px; line-height: 1.4;
  }
  .sanitising {
    position: absolute; left: 30px; top: 948px; width: 410px; text-align: center;
    color: var(--brand-green); font-weight: 700; font-size: 17px; line-height: 1.3;
  }

  .solutions-title {
    position: absolute; left: 500px; top: 640px;
    color: var(--white); font-weight: 800; font-size: 27px; letter-spacing: 0.5px;
  }
  .solutions {
    position: absolute; left: 470px; top: 700px; width: 400px;
    display: grid; grid-template-columns: 200px 200px; row-gap: 20px; list-style: none;
  }
  .solutions li {
    display: flex; align-items: center; gap: 10px;
    color: var(--white); font-weight: 600; font-size: 15px; line-height: 1.2; min-height: 42px;
  }
  .solutions svg { flex: none; }

  .contact-phone {
    position: absolute; left: 470px; top: 1070px; display: flex; align-items: center; gap: 12px;
    color: var(--white); font-family: "Roboto", Arial, sans-serif; font-size: 44px; font-weight: 400;
  }
  .contact-web {
    position: absolute; left: 470px; top: 1136px; width: 380px; text-align: right;
    color: var(--white); font-weight: 700; font-size: 19px;
  }
</style>
</head>
<body>
<main class="flyer">
  <svg class="flyer-backdrop" viewBox="0 0 877 1200">
    <defs>
      <linearGradient id="photoTone" x1="0" y1="0" x2="1" y2="1">
        <stop offset="0" stop-color="#15305e"/>
        <stop offset="0.45" stop-color="#4f6c8c"/>
        <stop offset="1" stop-color="#a9b4bd"/>
      </linearGradient>
      <linearGradient id="panelTone" x1="0" y1="0" x2="0" y2="1">
        <stop offset="0" stop-color="#00a990"/>
        <stop offset="0.35" stop-color="#0293ce"/>
        <stop offset="1" stop-color="#1d4fa0"/>
      </linearGradient>
      <linearGradient id="footerTone" x1="0" y1="0" x2="1" y2="0">
        <stop offset="0" stop-color="#163d80"/>
        <stop offset="1" stop-color="#1d4fa0"/>
      </linearGradient>
      <path id="badgeTop" d="M705 500 A70 70 0 0 1 845 500"/>
      <path id="badgeBottom" d="M693 500 A82 82 0 0 0 857 500"/>
    </defs>

    <rect class="site-photo" x="0" y="0" width="877" height="560" fill="url(#photoTone)"
          role="img" aria-label="Photo: two technicians in hi-vis workwear hot-water pressure cleaning the paving outside a large commercial building"/>

    <path class="right-panel" d="M455 470 C600 470 760 440 877 405 L877 1200 L455 1200 Z" fill="url(#panelTone)"/>
    <path class="wave-accent" d="M0 520 C200 440 460 520 877 400" fill="none" stroke="var(--sea-green)" stroke-width="12"/>
    <path class="white-field" d="M0 540 C150 478 330 478 460 505 L460 1200 L0 1200 Z" fill="#fff"/>

    <path class="footer-highlight" d="M0 1078 C250 1066 520 1010 877 990 L877 1006 C520 1026 250 1082 0 1094 Z" fill="#fff" opacity="0.8"/>
    <path class="footer-band" d="M0 1096 C250 1084 520 1028 877 1008 L877 1200 L0 1200 Z" fill="url(#footerTone)"/>

    <g class="response-badge">
      <circle cx="775" cy="500" r="96" fill="#fff"/>
      <circle cx="775" cy="500" r="89" fill="var(--deep-blue)"/>
      <circle cx="775" cy="500" r="58" fill="#fff"/>
      <text font-family="Open Sans, sans-serif" font-weight="800" font-size="14" fill="#fff" letter-spacing="1.5">
        <textPath href="#badgeTop" startOffset="50%" text-anchor="middle">READY TO RESPOND</textPath>
      </text>
      <text font-family="Open Sans, sans-serif" font-weight="800" font-size="14" fill="#fff" letter-spacing="1.5">
        <textPath href="#badgeBottom" startOffset="50%" text-anchor="middle">READY TO RESPOND</textPath>
      </text>
      <text x="775" y="475" text-anchor="middle" font-family="Open Sans, sans-serif" font-weight="700" font-size="11" fill="var(--deep-blue)">24 HOURS</text>
      <text x="775" y="518" text-anchor="middle" font-family="Open Sans, sans-serif" font-weight="800" font-size="40" fill="var(--deep-blue)">24/7</text>
      <text x="775" y="538" text-anchor="middle" font-family="Open Sans, sans-serif" font-weight="700" font-size="11" fill="var(--deep-blue)">7 DAYS</text>
    </g>
  </svg>

  <h1 class="headline">All Commercial &amp;<br>Industrial Property<br>Maintenace</h1>
  <p class="service-area">Servicing Southeast's Commercial &amp; Industrial sector 24/7</p>

  <div class="brand-name">
    <span class="initials">FLS</span>
    <span class="full">FERRO LANE &amp; SERVICES</span>
  </div>

  <p class="feature">SILENT HOT WATER PRESSURE CLEANING<span class="temp">Runs up to 120 Degrees Celsius</span></p>

  <ul class="assurances">
    <li><svg width="18" height="18" viewBox="0 0 18 18"><rect x="1" y="1" width="16" height="16" rx="2" fill="none" stroke="#0293ce" stroke-width="2"/><path d="M4 9 L8 13 L16 3" fill="none" stroke="#00a990" stroke-width="2.5"/></svg>Fully Accredited &amp; Certified Technicians</li>
    <li><svg width="18" height="18" viewBox="0 0 18 18"><rect x="1" y="1" width="16" height="16" rx="2" fill="none" stroke="#0293ce" stroke-width="2"/><path d="M4 9 L8 13 L16 3" fill="none" stroke="#00a990" stroke-width="2.5"/></svg>100% Satisfaction Guaranteed</li>
    <li><svg width="18" height="18" viewBox="0 0 18 18"><rect x="1" y="1" width="16" height="16" rx="2" fill="none" stroke="#0293ce" stroke-width="2"/><path d="M4 9 L8 13 L16 3" fill="none" stroke="#00a990" stroke-width="2.5"/></svg>Family owned and operated business</li>
    <li><svg width="18" height="18" viewBox="0 0 18 18"><rect x="1" y="1" width="16" height="16" rx="2" fill="none" stroke="#0293ce" stroke-width="2"/><path d="M4 9 L8 13 L16 3" fill="none" stroke="#00a990" stroke-width="2.5"/></svg>No job is too big or too small</li>
  </ul>

  <p class="equipment-note">All of our services are undertaken using industry leading equipment and, providing safe and superior results.</p>

  <p class="sanitising">SANITISING<br>Bin areas, outdoor areas, cafe's, restaurants, schools, drive thru's</p>

  <h2 class="solutions-title">SOLUTIONS FOR:</h2>
  <ul class="solutions">
    <li><svg width="34" height="34" viewBox="0 0 34 34"><circle cx="17" cy="17" r="9" fill="#33b8a4"/><g stroke="#33b8a4" stroke-width="2.5"><path d="M17 2v6M17 26v6M2 17h6M26 17h6M6 6l4 4M24 24l4 4M28 6l-4 4M6 28l4-4"/></g></svg>COVID-19 Infection Control</li>
    <li><svg width="34" height="34" viewBox="0 0 34 34" fill="#33b8a4"><circle cx="10" cy="10" r="5"/><circle cx="24" cy="9" r="4"/><circle cx="22" cy="23" r="6"/><circle cx="9" cy="24" r="3"/></svg>Common Area Cleaning</li>
    <li><svg width="34" height="34" viewBox="0 0 34 34" fill="#33b8a4"><rect x="4" y="8" width="12" height="24"/><rect x="18" y="2" width="12" height="30"/><g fill="#0293ce"><rect x="7" y="12" width="3" height="3"/><rect x="22" y="6" width="3" height="3"/><rect x="22" y="13" width="3" height="3"/><rect x="7" y="19" width="3" height="3"/></g></svg>Building Management</li>
    <li><svg width="34" height="34" viewBox="0 0 34 34" fill="#33b8a4"><path d="M10 4 C12 12 20 12 24 8 C22 16 28 18 30 14 C30 24 22 30 16 30 C10 30 4 24 6 16 Z"/></svg>Bird waste removal</li>
    <li><svg width="34" height="34" viewBox="0 0 34 34" fill="#33b8a4"><rect x="6" y="6" width="22" height="4" rx="1"/><path d="M8 12h18l-2 20H10z"/><rect x="13" y="2" width="8" height="3"/></svg>Bin Cleaning &amp; Sanitisation</li>
    <li><svg width="34" height="34" viewBox="0 0 34 34" fill="#33b8a4"><circle cx="17" cy="17" r="8"/><circle cx="8" cy="9" r="4"/><circle cx="27" cy="10" r="3"/><circle cx="26" cy="27" r="4"/><circle cx="7" cy="26" r="3"/></svg>Mould &amp; Mildew removal</li>
    <li><svg width="34" height="34" viewBox="0 0 34 34" fill="#33b8a4"><path d="M17 30V14" stroke="#33b8a4" stroke-width="3"/><path d="M17 16C8 16 5 8 6 4c8 0 11 6 11 12zM17 16c9 0 12-8 11-12-8 0-11 6-11 12z"/><rect x="6" y="28" width="22" height="3"/></svg>Garden Maintenance</li>
    <li><svg width="34" height="34" viewBox="0 0 34 34" fill="#33b8a4"><path d="M17 3C12 12 8 17 8 22a9 9 0 0 0 18 0c0-5-4-10-9-19z"/></svg>Oil and Grease elimination</li>
  </ul>

  <p class="contact-phone">
    <svg width="44" height="44" viewBox="0 0 44 44"><circle cx="22" cy="22" r="19" fill="none" stroke="#fff" stroke-width="3"/><path d="M14 12c2-1 4 3 5 5 1 2-2 3-1 5 1 2 3 4 5 5 2 1 3-2 5-1 2 1 6 3 5 5-1 3-4 4-7 3-6-2-11-7-13-13-1-3 0-8 1-9z" fill="#fff"/></svg>
    1300 555 014
  </p>
  <p class="contact-web">www.ferrolaneservices.au</p>
</main>
</body>
</html>
```